Business card for auto dealership

Looking for a clean modern design.
Would like attached logo incorporated

Industry/Entity Type

Car dealership

Contact Information for Business Card

Name, website, phone, cell, fax, email

```html
<!DOCTYPE html>
<html lang="en">
<head>
<meta charset="utf-8">
<title>Halvorsen Auto – Business Card</title>
<link rel="stylesheet" href="https://fonts.googleapis.com/css2?family=Open+Sans:wght@400&family=Roboto+Condensed:wght@700&display=swap">
<style>
  :root {
    --backdrop: #e6e6e6;
    --card: #2b2b2b;
    --emboss: #1b1b1b;
    --ink: #ffffff;
    --ink-soft: #e8e8e8;
  }
  * { margin: 0; padding: 0; box-sizing: border-box; }
  html, body { width: 1200px; height: 960px; overflow: hidden; }
  body { background: var(--backdrop); position: relative; font-family: "Open Sans", sans-serif; }

  .card {
    position: absolute;
    left: 295px;
    width: 613px;
    height: 350px;
    background: var(--card);
  }
  .card--front { top: 103px; }
  .card--back { top: 507px; }

  .brand-name {
    font-family: "Roboto Condensed", sans-serif;
    font-weight: 700;
    white-space: nowrap;
    line-height: 1;
  }
  .card--front .brand-name {
    position: absolute;
    left: 0; right: 0; top: 140px;
    text-align: center;
    font-size: 64px;
    color: var(--emboss);
  }
  .card--back .brand-name {
    position: absolute;
    left: 41px; top: 52px;
    font-size: 44px;
    color: var(--ink);
  }

  .holder {
    position: absolute;
    right: 41px; top: 155px;
    text-align: right;
  }
  .holder__name {
    font-family: "Roboto Condensed", sans-serif;
    font-weight: 700;
    font-size: 27px;
    line-height: 32px;
    color: var(--ink);
  }
  .holder__title {
    font-size: 14px;
    line-height: 20px;
    color: var(--ink-soft);
    margin-top: 2px;
  }
  .divider {
    position: absolute;
    left: 41px; top: 197px;
    width: 399px; height: 1px;
    background: var(--ink);
  }

  .contact-list {
    position: absolute;
    left: 41px; top: 218px;
    list-style: none;
  }
  .contact-list li {
    display: flex;
    align-items: center;
    height: 20.5px;
    font-size: 14px;
    color: var(--ink-soft);
  }
  .contact-list svg {
    width: 14px; height: 14px;
    margin-right: 7px;
    fill: none;
    stroke: var(--ink);
    stroke-width: 1.5;
  }
</style>
</head>
<body>
  <section class="card card--front">
    <div class="brand-name">Halvorsen Auto</div>
  </section>

  <section class="card card--back">
    <div class="brand-name">Halvorsen Auto</div>

    <div class="holder">
      <div class="holder__name">Dana Halvorsen</div>
      <div class="holder__title">Founder &amp; Owner</div>
    </div>
    <div class="divider"></div>

    <ul class="contact-list">
      <li>
        <svg viewBox="0 0 14 14" aria-hidden="true"><path d="M3 1.5 L5 4 L4 5.5 Q5.5 8.5 8.5 10 L10 9 L12.5 11 L11 13 Q5 12 1 3 Z"/></svg>
        555-014-2201
      </li>
      <li>
        <svg viewBox="0 0 14 14" aria-hidden="true"><rect x="3.5" y="1" width="7" height="12" rx="1"/><line x1="6" y1="11" x2="8" y2="11"/></svg>
        555-017-3380
      </li>
      <li>
        <svg viewBox="0 0 14 14" aria-hidden="true"><rect x="4" y="1" width="6" height="4"/><rect x="1" y="5" width="12" height="5"/><rect x="4" y="9" width="6" height="4"/></svg>
        555-019-4475
      </li>
      <li>
        <svg viewBox="0 0 14 14" aria-hidden="true"><rect x="1" y="3" width="12" height="8"/><path d="M1 3 L7 8 L13 3"/></svg>
        dana@halvorsenauto.com
      </li>
      <li>
        <svg viewBox="0 0 14 14" aria-hidden="true"><circle cx="7" cy="7" r="5.8"/><ellipse cx="7" cy="7" rx="2.5" ry="5.8"/><line x1="1.2" y1="7" x2="12.8" y2="7"/></svg>
        www.Halvorsenauto.com
      </li>
    </ul>
  </section>
</body>
</html>
```